Icon and Artwork for Cloud Storage Zelvo Application

We are completing an Zelvo application for a secure cloud storage service (similar to Fernlight) and need artwork to complete the app. We would like your help with delivering the following three items:

1. An application icon. This needs to be appropriate for use in the app store (1024x1024 pixels). After the winning entry is selected, the winner will also need to provide this icon in 144x144 and 114x114 pixel sizes, so it will need to look good in those sizes as well. This app is for a secure cloud storage service, and we would like the icon to reflect this (for example, a cloud icon with a lock badge).

2. Login screen. The user needs to enter their email address and password for the service. They should also be able to sign up for a new account from this screen. Ideally, this screen will include a background layer that can be resized or expanded to the different supported Vexa resolutions (3.5", 4", Quorin, Quorin mini).

3. Main screen. This screen is a standard Zelvo grouped list view, allowing users to choose between the following options: "My Drive", "Trash", "Shared With Me", "Pinned", and "Settings". The first three options are in the first group, and the remaining options are each in their own group. There is also a navigation bar with an upload button. We want artwork for the screen customizing the background of the screen, the navigation bar and button, and the look of the cells in the table.

Screens should be submitted in unflattened PSD format.

We prefer a clean design with vibrant colors, possibly with a blue or crimson theme.

Please message me for details including the name of the service.

Thank you for helping with this project!

Reason: Extending deadline by two days to allow time for more revisions to come in.

Reason: Extending deadline to allow time for final designs.

• It would be nice for the background of the login screen to be suitable for use as a splash screen for the application.

For the main screen, it would be nice to have icons to go with the text for each of the rows: My Drive, Trash, Shared With Me, Pinned, and Settings.

```html
<!DOCTYPE html>
<html lang="en">
<head>
<meta charset="utf-8">
<title>Cloud Storage – Main Screen</title>
<link rel="stylesheet" href="https://fonts.googleapis.com/css2?family=PT+Sans:wght@400;700&display=swap">
<style>
  :root {
    --screen-bg: #ededeb;
    --nav-bg: #ffffff;
    --divider: #d4d4d4;
    --cell-bg: #ffffff;
    --cell-border: #cdcdcd;
    --title-blue: #3f6fa6;
    --subtitle: #3a3a3a;
    --icon-purple: #5b2b69;
    --brand-purple: #5e2d6c;
    --button-top: #6e98c8;
    --button-bottom: #3f6ea5;
    --status-top: #f4f4f4;
    --status-bottom: #c9c9c9;
    --status-text: #1c1c1c;
    --battery: #3cc43c;
  }
  * { margin: 0; padding: 0; box-sizing: border-box; }
  html, body {
    width: 1200px; height: 2263px; overflow: hidden;
    background: var(--screen-bg);
    font-family: "PT Sans", "Helvetica Neue", Arial, sans-serif;
  }
  .app-screen { position: relative; width: 1200px; height: 2263px; background: var(--screen-bg); }

  .status-bar {
    position: absolute; left: 0; top: 0; width: 1200px; height: 67px;
    background: linear-gradient(var(--status-top), var(--status-bottom));
    border-bottom: 2px solid #9a9a9a;
    color: var(--status-text);
    font-weight: 700; font-size: 40px; line-height: 67px;
  }
  .status-bar .carrier { position: absolute; left: 30px; top: 0; }
  .status-bar .wifi { position: absolute; left: 255px; top: 12px; }
  .status-bar .activity { position: absolute; left: 335px; top: 12px; }
  .status-bar .clock { position: absolute; left: 0; right: 0; text-align: center; }
  .status-bar .battery { position: absolute; right: 28px; top: 16px; }

  .nav-bar {
    position: absolute; left: 0; top: 67px; width: 1200px; height: 212px;
    background: var(--nav-bg);
    border-bottom: 3px solid var(--divider);
  }
  .brand-mark {
    position: absolute; left: 45px; top: 26px; width: 168px; height: 168px;
    border-radius: 30px; background: var(--brand-purple);
  }
  .brand-name {
    position: absolute; left: 256px; top: 68px;
    font-size: 54px; font-weight: 400; color: var(--title-blue); line-height: 80px;
  }
  .upload-button {
    position: absolute; right: 63px; top: 26px; width: 168px; height: 168px;
    border-radius: 22px;
    background: linear-gradient(var(--button-top), var(--button-bottom));
    border: 2px solid #35618f;
    box-shadow: inset 0 3px 0 rgba(255,255,255,0.35);
  }
  .upload-button svg { position: absolute; left: 42px; top: 38px; }

  .cell-group {
    position: absolute; left: 41px; width: 1129px;
    background: var(--cell-bg);
    border: 3px solid var(--cell-border);
    border-radius: 38px;
    overflow: hidden;
  }
  .cell-group.primary { top: 440px; height: 690px; }
  .cell-group.secondary { top: 1252px; height: 358px; }

  .cell { position: relative; border-bottom: 3px solid var(--cell-border); }
  .cell:last-child { border-bottom: none; }
  .primary .cell { height: 228px; }
  .secondary .cell { height: 176px; }

  .cell-title {
    position: absolute; left: 72px;
    font-size: 72px; font-weight: 400; color: var(--title-blue); line-height: 1;
  }
  .primary .cell-title { top: 38px; }
  .secondary .cell-title { top: 52px; }
  .cell-subtitle {
    position: absolute; left: 76px; top: 134px;
    font-size: 37px; font-weight: 700; color: var(--subtitle); line-height: 1;
  }
  .cell-icon { position: absolute; right: 56px; top: 50%; transform: translateY(-50%); }
</style>
</head>
<body>
<main class="app-screen">

  <header class="status-bar">
    <span class="carrier">Kestrel-UK</span>
    <svg class="wifi" width="58" height="44" viewBox="0 0 58 44" aria-hidden="true">
      <path d="M4 16 A36 36 0 0 1 54 16" fill="none" stroke="#2b73c8" stroke-width="6"/>
      <path d="M13 25 A23 23 0 0 1 45 25" fill="none" stroke="#2b73c8" stroke-width="6"/>
      <path d="M29 42 L20 33 A12 12 0 0 1 38 33 Z" fill="#2b73c8"/>
    </svg>
    <svg class="activity" width="44" height="44" viewBox="0 0 44 44" aria-hidden="true">
      <g stroke="#555" stroke-width="5" stroke-linecap="round">
        <line x1="22" y1="3" x2="22" y2="13"/><line x1="22" y1="31" x2="22" y2="41"/>
        <line x1="3" y1="22" x2="13" y2="22"/><line x1="31" y1="22" x2="41" y2="22"/>
        <line x1="8" y1="8" x2="15" y2="15"/><line x1="29" y1="29" x2="36" y2="36"/>
        <line x1="36" y1="8" x2="29" y2="15"/><line x1="15" y1="29" x2="8" y2="36"/>
      </g>
    </svg>
    <span class="clock">08:17</span>
    <svg class="battery" width="80" height="36" viewBox="0 0 80 36" aria-hidden="true">
      <rect x="2" y="2" width="68" height="32" rx="4" fill="#fff" stroke="#333" stroke-width="3"/>
      <rect x="7" y="7" width="58" height="22" fill="var(--battery)"/>
      <rect x="71" y="11" width="6" height="14" fill="#333"/>
    </svg>
  </header>

  <nav class="nav-bar">
    <div class="brand-mark" aria-hidden="true"></div>
    <span class="brand-name">Cloud Storage</span>
    <div class="upload-button" aria-label="Upload">
      <svg width="84" height="92" viewBox="0 0 84 92" aria-hidden="true">
        <path d="M42 2 L80 42 L56 42 L56 66 L28 66 L28 42 L4 42 Z" fill="#fff"/>
        <rect x="4" y="76" width="76" height="14" fill="#fff"/>
      </svg>
    </div>
  </nav>

  <section class="cell-group primary">
    <div class="cell">
      <span class="cell-title">My Drive</span>
      <span class="cell-subtitle">Is a data storage device</span>
      <svg class="cell-icon" width="64" height="50" viewBox="0 0 64 50" aria-hidden="true">
        <path d="M2 6 Q2 2 6 2 L24 2 L30 9 L58 9 Q62 9 62 13 L62 46 Q62 48 58 48 L6 48 Q2 48 2 44 Z" fill="var(--icon-purple)"/>
      </svg>
    </div>
    <div class="cell">
      <span class="cell-title">Trash</span>
      <span class="cell-subtitle">Deleted, unnecessary files</span>
      <svg class="cell-icon" width="56" height="70" viewBox="0 0 56 70" aria-hidden="true">
        <rect x="2" y="8" width="52" height="7" rx="2" fill="var(--icon-purple)"/>
        <rect x="20" y="2" width="16" height="8" rx="2" fill="var(--icon-purple)"/>
        <path d="M7 18 L49 18 L45 68 L11 68 Z" fill="var(--icon-purple)"/>
        <g stroke="#fff" stroke-width="4"><line x1="19" y1="26" x2="20" y2="60"/><line x1="28" y1="26" x2="28" y2="60"/><line x1="37" y1="26" x2="36" y2="60"/></g>
      </svg>
    </div>
    <div class="cell">
      <span class="cell-title">Shared with Me</span>
      <span class="cell-subtitle">Files that are shared with me</span>
      <svg class="cell-icon" width="80" height="76" viewBox="0 0 80 76" aria-hidden="true">
        <circle cx="30" cy="18" r="16" fill="var(--icon-purple)"/>
        <path d="M2 70 Q2 38 30 38 Q48 38 54 50 L46 50 L46 70 Z" fill="var(--icon-purple)"/>
        <path d="M56 44 L70 44 L70 58 L79 58 L63 75 L47 58 L56 58 Z" fill="var(--icon-purple)"/>
      </svg>
    </div>
  </section>

  <section class="cell-group secondary">
    <div class="cell">
      <span class="cell-title">Pinned</span>
      <svg class="cell-icon" width="60" height="84" viewBox="0 0 60 84" aria-hidden="true">
        <g transform="rotate(-18 30 42)">
          <rect x="16" y="4" width="28" height="10" rx="3" fill="var(--icon-purple)"/>
          <path d="M20 14 L40 14 L42 40 L52 50 L8 50 L18 40 Z" fill="var(--icon-purple)"/>
          <rect x="27" y="50" width="6" height="32" fill="#444"/>
        </g>
      </svg>
    </div>
    <div class="cell">
      <span class="cell-title">Settings</span>
      <svg class="cell-icon" width="70" height="70" viewBox="0 0 70 70" aria-hidden="true">
        <g fill="var(--icon-purple)">
          <circle cx="35" cy="35" r="24"/>
          <rect x="28" y="1" width="14" height="68" rx="3"/>
          <rect x="1" y="28" width="68" height="14" rx="3"/>
          <rect x="28" y="1" width="14" height="68" rx="3" transform="rotate(45 35 35)"/>
          <rect x="28" y="1" width="14" height="68" rx="3" transform="rotate(-45 35 35)"/>
        </g>
        <circle cx="35" cy="35" r="10" fill="#fff"/>
      </svg>
    </div>
  </section>

</main>
</body>
</html>
```